Website Online Research Solutions

We are a small European high-tech online research company.
With our own state of the art software we run online panels and are conducting reseach for companies. Partly research via our own panel and partly via panels we maintain for our customers.
Our current website is old and outdatet: www.velmora.nl.
We are in the process to change the content of the site. We want a modern, european and businesslike design for our new website.
Our logo has to stay the same (left uppersite of our website and attached) but can be changed a little to adapt it to the new design of the website. The colors of the site are up to you.
Target Market(s)
Marketeers and researchers of large and middle size companies in all kind of fields.
Industry/Entity Type
Online
Look and feel
Each slider illustrates characteristics of the customer's brand and the style your logo design should communicate.

```html
<!DOCTYPE html>
<html lang="nl">
<head>
<meta charset="utf-8">
<title>Velmora – Online Research Solutions</title>
<link rel="stylesheet" href="https://fonts.googleapis.com/css2?family=Arimo:wght@400;700&family=Open+Sans:wght@400;600&display=swap">
<style>
:root{
  --navy:#0f2550;
  --navy-deep:#081634;
  --red:#b3060c;
  --red-bright:#d81a1a;
  --text:#0f2a5a;
  --grey-text:#555;
  --panel:#f1f1f1;
  --card:#ececec;
  --border:#c9c9c9;
  --footer:#1c1c1c;
  --footer-bar:#2b2b2b;
  --footer-text:#c8c8c8;
}
*{box-sizing:border-box;margin:0;padding:0}
html,body{width:928px;height:1200px;overflow:hidden}
body{font-family:"Arimo",Arial,sans-serif;background:#efefef;position:relative;color:var(--text)}
.abs{position:absolute}

.site-header{left:0;top:0;width:928px;height:90px;background:radial-gradient(ellipse at 50% 0,#3e5685 0,#1a3265 45%,var(--navy-deep) 100%);border-bottom:3px solid var(--red)}
.brand{left:126px;top:14px;width:122px;height:122px;border-radius:50%;background:#f4f4f4;border:3px solid #9a9a9a;display:flex;align-items:center;justify-content:center;z-index:3}
.brand span{font-family:"Open Sans",sans-serif;font-weight:600;font-size:20px;color:#333;letter-spacing:1px}
.main-nav{left:331px;top:57px;display:flex;gap:5px}
.main-nav a{width:63px;height:31px;border-radius:5px 5px 0 0;background:linear-gradient(#a6adb9,#7f8795);color:#fff;font-size:11px;text-decoration:none;display:flex;align-items:center;justify-content:center}
.main-nav a.active{background:linear-gradient(#c8141a,#8e0508)}

.hero{left:0;top:90px;width:928px;height:272px;background:linear-gradient(160deg,#ffffff 0,#ececec 60%,#dcdcdc 100%);border-bottom:4px solid #9aa0aa}
.hero-map{left:380px;top:122px;width:400px;height:200px;border-radius:30px;background:radial-gradient(ellipse,#c9c9c9 0,rgba(220,220,220,0) 70%)}
.hero-photo{left:514px;top:120px;width:257px;height:242px;background:linear-gradient(180deg,#d9d3cc 0,#6d6a6a 45%,#1c1c1e 100%);border-radius:60px 60px 0 0}
.hero-title{left:145px;top:160px;font-family:"Open Sans",sans-serif;font-size:25px;line-height:31px;color:#444;font-weight:400}
.hero-title em{font-style:normal;color:var(--red)}
.hero-copy{left:148px;top:236px;width:345px;font-size:10px;line-height:14px;color:#333}
.btn{top:297px;width:124px;height:30px;border-radius:3px;color:#fff;font-size:14px;display:flex;align-items:center;justify-content:center;box-shadow:0 1px 2px rgba(0,0,0,.4)}
.btn-dark{left:153px;background:linear-gradient(#4a4a4a,#0d0d0d)}
.btn-red{left:290px;background:linear-gradient(var(--red-bright),#8d0306)}

.section-tab{height:20px;background:var(--navy);color:#fff;font-size:9px;display:flex;align-items:center;justify-content:center;border-radius:0 0 9px 9px;z-index:2}
.tab-products{left:406px;top:362px;width:110px}
.products{left:0;top:366px;width:928px;height:179px;background:#f6f6f6;box-shadow:0 8px 10px -8px #bbb}
.product-card{top:408px;width:144px;height:118px;border:1px solid var(--border);border-radius:3px;background:linear-gradient(#f7f7f7,#e4e4e4)}
.product-card .icon{position:absolute;left:44px;top:20px;width:56px;height:46px;border-radius:6px}
.product-card p{position:absolute;left:0;right:0;top:92px;text-align:center;font-size:10.5px;color:#222}

.col-title{top:574px;font-size:19px;color:var(--text);font-weight:400}
.about-box{left:131px;top:610px;width:310px;height:217px;border:1px solid var(--border);border-radius:6px;background:#f7f7f7}
.about-photo{left:151px;top:624px;width:271px;height:80px;background:linear-gradient(90deg,#7d6f63,#c9c4bd 40%,#5f6f85 80%,#2d3b55);border:3px solid #fff;outline:1px solid #ddd}
.about-copy{left:156px;top:720px;width:272px;font-size:9px;line-height:17.5px;color:var(--text)}
.about-more{left:371px;top:801px;font-size:9.5px;color:var(--red);text-decoration:underline}
.col-divider{left:464px;top:597px;width:1px;height:232px;background:#ccc}
.quote-box{left:487px;top:616px;width:311px;height:114px;border:1px solid var(--border);border-radius:6px;background:#f7f7f7}
.quote-mark{left:504px;top:618px;font-family:Georgia,serif;font-size:64px;color:#b8b8b8}
.quote-text{left:550px;top:634px;width:232px;font-size:9px;line-height:17.5px;color:var(--text)}
.quote-by{left:616px;top:698px;font-size:9px;color:var(--text)}
.quote-by b{font-weight:400;color:var(--red)}
.quote-by i{font-style:italic}
.media-box{left:487px;top:748px;width:311px;height:72px;border:1px solid var(--border);border-radius:6px;background:linear-gradient(#fff,#e6e6e6);overflow:hidden}
.media-photo{left:490px;top:751px;width:90px;height:66px;background:linear-gradient(135deg,#8a6d4f,#d8bc8f 55%,#5b4634)}
.media-play{left:556px;top:777px}
.media-title{left:597px;top:766px;font-size:18px;color:#222}
.media-rule{left:597px;top:789px;width:160px;height:1px;background:#bbb}
.media-sub{left:597px;top:794px;font-size:7.5px;color:#222}

.tab-clients{left:412px;top:858px;width:108px;border-radius:9px 9px 0 0}
.clients{left:133px;top:877px;width:665px;height:92px;border:1px solid var(--border);border-radius:12px;background:#f8f8f8}
.client{top:896px;height:56px;display:flex;align-items:center;gap:5px;font-size:13px;font-weight:700}
.client i{display:block;width:10px;height:10px}
.arrow{top:918px}

.site-footer{left:0;top:992px;width:928px;height:168px;background:linear-gradient(#222,#151515)}
.footer-col h3{font-size:13px;font-weight:700;color:#9a9a9a;margin-bottom:6px}
.footer-col li,.footer-col p{list-style:none;font-size:9px;line-height:17.7px;color:var(--footer-text)}
.sitemap li::before{content:"";display:inline-block;width:3px;height:3px;background:var(--red-bright);margin:0 12px 2px 4px}
.social li span{display:inline-block;width:13px;height:13px;border-radius:2px;background:#3a86c8;margin-right:10px;vertical-align:-3px}
.social li{line-height:22px}
.footer-rule{top:1008px;width:1px;height:130px;background:#333}
.footer-brand{left:663px;top:1020px;width:100px;height:100px;border-radius:50%;background:#e9e9e9;border:2px solid #888;display:flex;align-items:center;justify-content:center;font-family:"Open Sans",sans-serif;font-weight:600;font-size:15px;color:#333}
.footer-bar{left:0;top:1160px;width:928px;height:40px;background:var(--footer-bar);color:#ddd;font-size:9px;display:flex;align-items:center;justify-content:center}
</style>
</head>
<body>

<header class="site-header abs"></header>
<div class="brand abs"><span>VELMORA</span></div>
<nav class="main-nav abs">
  <a class="active">Algemeen</a><a>Producten</a><a>Demo's</a><a>Media</a><a>Referenties</a><a>Personeel</a><a>Contact</a>
</nav>

<section class="hero abs"></section>
<div class="hero-map abs" role="img" aria-label="Gestippelde wereldkaart"></div>
<div class="hero-photo abs" role="img" aria-label="Foto van twee zakelijke medewerkers"></div>
<h1 class="hero-title abs"><em>Velmora</em> is gespecialiseerd in<br>online gegevensverzameling.</h1>
<p class="hero-copy abs">Lorem ipsum dolor sit amet, consectetur adipiscing elit. Aenean ligula justo, faucibus a imperdiet vitae, vestibulum at diam. Proin ac nulla lorem, ac cursus lectus. In in est sed felis mattis oin ac nulla lorem.</p>
<div class="btn btn-dark abs">Read More</div>
<div class="btn btn-red abs">Try Demo</div>

<section class="products abs"></section>
<div class="section-tab tab-products abs">Producten</div>
<div class="product-card abs" style="left:162px"><div class="icon" role="img" aria-label="Illustratie van databaseservers" style="background:linear-gradient(#e8eef6,#9bb0c9)"></div><p>Dataverzameling</p></div>
<div class="product-card abs" style="left:314px"><div class="icon" role="img" aria-label="Illustratie van een stijgende grafiek" style="background:linear-gradient(#fff6d6,#e2634a)"></div><p>Analyse</p></div>
<div class="product-card abs" style="left:465px"><div class="icon" role="img" aria-label="Illustratie van een monitor met diagrammen" style="background:linear-gradient(#6fb2ee,#1d4f9a)"></div><p>Dataset Publishing</p></div>
<div class="product-card abs" style="left:619px"><div class="icon" role="img" aria-label="Illustratie van panelleden" style="background:linear-gradient(#f3c07a,#5b9a3c)"></div><p>Panel Pollaris</p></div>

<h2 class="col-title abs" style="left:148px">About Us</h2>
<h2 class="col-title abs" style="left:487px">Referenties</h2>
<div class="about-box abs"></div>
<div class="about-photo abs" role="img" aria-label="Foto van het kantoor met medewerkers achter computers"></div>
<p class="about-copy abs">Lorem ipsum dolor sit amet, consectetur adipiscing elit. Maecenas luctus est non neque placerat nec consequat diam porta. Pellen-tesque habitant morbi tristique senectus et netus et malesuada fames ac turpis egestas. Sed vulputate dapibus ipsum</p>
<a class="about-more abs">Read More</a>
<div class="col-divider abs"></div>

<div class="quote-box abs"></div>
<div class="quote-mark abs">“</div>
<p class="quote-text abs">Velmora biedt ons een zeer flexibele, snelle en efficiente onderzoekstool. Hiermee sluiten ze uitstekend aan bij de behoeften van onze marketeers.</p>
<p class="quote-by abs"><b>Joris Veldman</b> - <i>CIM Harwell Food Group</i></p>

<div class="media-box abs"></div>
<div class="media-photo abs" role="img" aria-label="Foto van een spreker aan een bureau"></div>
<svg class="media-play abs" width="26" height="26" viewBox="0 0 26 26"><circle cx="13" cy="13" r="12" fill="#4fa83a" stroke="#fff" stroke-width="2"/><path d="M7 13h9M12 8l5 5-5 5" stroke="#fff" stroke-width="2.5" fill="none"/></svg>
<div class="media-title abs">Media Archived</div>
<div class="media-rule abs"></div>
<div class="media-sub abs">ADSL, Cable (500Kbps)&nbsp; ISDN, Analog (56Kbps)</div>

<div class="section-tab tab-clients abs">KLANTEN</div>
<div class="clients abs"></div>
<svg class="arrow abs" style="left:150px" width="14" height="14" viewBox="0 0 14 14"><circle cx="7" cy="7" r="7" fill="#333"/><path d="M8.5 4 5 7l3.5 3z" fill="#fff"/></svg>
<svg class="arrow abs" style="left:764px" width="14" height="14" viewBox="0 0 14 14"><circle cx="7" cy="7" r="7" fill="#333"/><path d="M5.5 4 9 7l-3.5 3z" fill="#fff"/></svg>
<div class="client abs" style="left:186px;color:#1d3a8a"><i style="background:#f08a00;border-radius:50%"></i>Dalbrook</div>
<div class="client abs" style="left:268px;color:#d4142a">Kester &amp; Holm</div>
<div class="client abs" style="left:375px;color:#1f8fd0"><i style="background:#1f8fd0"></i>Ovenda</div>
<div class="client abs" style="left:470px;color:#3a3a8a">Brightfold<i style="background:#7b4fb3;border-radius:50%"></i></div>
<div class="client abs" style="left:600px;color:#1a6fb8">Lumo</div>
<div class="client abs" style="left:695px;color:#8ab520"><i style="background:#a9c61a"></i>Varo</div>

<footer class="site-footer abs"></footer>
<div class="footer-col abs" style="left:131px;top:1012px">
  <h3>Address</h3>
  <p>Velmora BV<br>Havenkade 12<br>1012 AB Lindewaard<br>tel +31 (0)20 555 0140<br>fax +31 (0)20 555 0141<br>info@velmora.nl</p>
</div>
<div class="footer-rule abs" style="left:276px"></div>
<div class="footer-col sitemap abs" style="left:320px;top:1012px">
  <h3>Sitemap</h3>
  <ul><li>Algemeen</li><li>Producten</li><li>Demo's</li><li>Media</li><li>Referenties</li><li>Personeel</li></ul>
</div>
<div class="footer-rule abs" style="left:441px"></div>
<div class="footer-col social abs" style="left:490px;top:1012px">
  <h3>Social Media</h3>
  <ul><li><span></span>Chirper</li><li><span></span>Facepage</li><li><span></span>Linkwork</li></ul>
</div>
<div class="footer-rule abs" style="left:616px"></div>
<div class="footer-brand abs">VELMORA</div>
<div class="footer-bar abs">Copyright © 2010 Velmora. Al Right Reserved,</div>

</body>
</html>
```